Building company buisness cards

We are looking for a sharp modern new look for our business cards.We are a New Zealand based company that specialises in house and land packages.We have attached a photo of the current logo and would like to see if it can be improved somehow if needed.We are open to any colours but we have chosen Black and White at this stage. Feel free to change the font and make the logo smarter looking.Play with the colours and see what looks best.We want a card that looks so good know one will want to throw it away!

Target Market(s)

Building profesonals, home buyers

Industry/Entity Type

Building

Contact Information for Business Card

Derek Haskins
0274930268
derekh@stonerange.co.nz

Font styles to use
Serif
Sans Serif

Colors

Designer to choose colors to be used in the design.

Requirements
Must have
• Just the logo on one side and details on the other
• Clean simple looking card
Nice to have
• Round corners and detail like raised or spot UV
• Something that stands out
Should not have
• To title needed, Director etc

```html
<!DOCTYPE html>
<html lang="en">
<head>
<meta charset="utf-8">
<title>Stonerange Business Card</title>
<link href="https://fonts.googleapis.com/css2?family=Open+Sans:wght@400;600;700&display=swap" rel="stylesheet">
<style>
  :root {
    --backdrop: #e5e4e9;
    --card-light: #ffffff;
    --card-dark: #171717;
    --ink: #111111;
    --ink-soft: #444444;
    --rule: #555555;
    --paper: #ffffff;
  }
  * { margin: 0; padding: 0; box-sizing: border-box; }
  html, body {
    width: 1200px; height: 1200px; overflow: hidden;
    background: var(--backdrop);
    font-family: "Open Sans", Arial, sans-serif;
  }
  .canvas { position: relative; width: 1200px; height: 1200px; }
  .card {
    position: absolute; left: 265px; width: 668px; height: 401px;
  }
  .card--front { top: 170px; background: var(--card-light); }
  .card--back { top: 607px; background: var(--card-dark); }

  .wordmark {
    display: flex; align-items: center; gap: 10px;
    font-weight: 700; letter-spacing: -0.5px; white-space: nowrap;
  }
  .wordmark__dot {
    border-radius: 50%; border: 2px solid currentColor; flex: none;
  }
  .card--front .wordmark {
    position: absolute; left: 0; width: 331px; top: 180px;
    justify-content: center; color: var(--ink); font-size: 36px; line-height: 1;
  }
  .card--front .wordmark__dot { width: 44px; height: 44px; }

  .divider {
    position: absolute; left: 330px; top: 93px; width: 2px; height: 215px;
    background: var(--rule);
  }
  .contact { position: absolute; left: 376px; top: 142px; color: var(--ink); }
  .contact__name { font-size: 27px; font-weight: 600; line-height: 1; margin-bottom: 26px; }
  .contact__row {
    display: flex; align-items: center; height: 24px; margin-bottom: 15px;
    font-size: 17px; color: var(--ink-soft);
  }
  .contact__icon { width: 20px; height: 24px; margin-left: -19px; margin-right: 26px; flex: none; }

  .card--back .wordmark {
    position: absolute; left: 0; right: 0; top: 146px;
    justify-content: center; color: var(--paper); font-size: 30px; line-height: 1;
  }
  .card--back .wordmark__dot { width: 40px; height: 40px; }
  .back-rule {
    position: absolute; left: 309px; top: 206px; width: 60px; height: 1px;
    background: var(--paper);
  }
  .web {
    position: absolute; left: 0; right: 0; top: 226px; text-align: center;
    color: var(--paper); font-size: 18px;
  }
</style>
</head>
<body>
<div class="canvas">
  <section class="card card--front">
    <div class="wordmark"><span>Stonerange</span><span class="wordmark__dot"></span></div>
    <div class="divider"></div>
    <div class="contact">
      <p class="contact__name">Derek Haskins</p>
      <div class="contact__row">
        <svg class="contact__icon" viewBox="0 0 20 24" aria-hidden="true">
          <rect x="3" y="1" width="14" height="22" rx="1.5" fill="none" stroke="#555" stroke-width="1.2"/>
          <line x1="3" y1="4.5" x2="17" y2="4.5" stroke="#555" stroke-width="1"/>
          <line x1="3" y1="19" x2="17" y2="19" stroke="#555" stroke-width="1"/>
          <line x1="8.5" y1="21" x2="11.5" y2="21" stroke="#555" stroke-width="1"/>
        </svg>
        <span>0274930268</span>
      </div>
      <div class="contact__row">
        <svg class="contact__icon" viewBox="0 0 20 24" aria-hidden="true">
          <circle cx="10" cy="12" r="3.6" fill="none" stroke="#555" stroke-width="1.2"/>
          <path d="M13.6 9v4.2c0 1.6 2.6 1.9 3.2-.4.9-4-1.6-8-6.3-8A7.2 7.2 0 1 0 14.5 18" fill="none" stroke="#555" stroke-width="1.2"/>
        </svg>
        <span>derekh@stonerange.co.nz</span>
      </div>
    </div>
  </section>

  <section class="card card--back">
    <div class="wordmark"><span>Stonerange</span><span class="wordmark__dot"></span></div>
    <div class="back-rule"></div>
    <p class="web">www.stonerange.co.nz</p>
  </section>
</div>
</body>
</html>
```